I am looking for a book cover designs. The title of the book is "Ways to stand out and where your habits slip"

the book is not too formal but it is also not informal.

I wish for the title to be easily readable and capturing, especially the "ways to stand out" part.

the book should also include the author name: Tobar Kessly

everyone

• Full title and author name: Tobar Kessly
• There is a chapter that is called "turn the lamp inward", if you wish to do an illustration as part of the cover then perhaps that can give you an idea of what to go with.
• anything that takes attention away from the title.Also should not include any photographs.

```html
<!DOCTYPE html>
<html lang="en">
<head>
<meta charset="utf-8">
<title>Ways to Stand Out — Cover Spread</title>
<link rel="stylesheet" href="https://fonts.googleapis.com/css2?family=Bebas+Neue&family=Merriweather:wght@400;700&display=swap">
<style>
  :root {
    --cover-blue: #1a8fc1;
    --cover-blue-deep: #1583b3;
    --cover-blue-light: #2ea3d4;
    --ink: #0c0e12;
    --paper: #ffffff;
    --stage: #e4e5e7;
    --title-font: "Bebas Neue", "Oswald", sans-serif;
    --text-font: "Merriweather", Georgia, serif;
  }
  * { box-sizing: border-box; margin: 0; padding: 0; }
  html, body {
    width: 1200px;
    height: 781px;
    overflow: hidden;
    background: var(--stage);
  }
  .spread {
    position: absolute;
    left: 40px;
    top: 44px;
    width: 1120px;
    height: 692px;
    display: flex;
    box-shadow: 0 2px 8px rgba(0,0,0,0.25);
  }
  .back-cover, .front-cover {
    position: relative;
    width: 527px;
    height: 100%;
    overflow: hidden;
    background:
      radial-gradient(ellipse 60% 30% at 30% 15%, rgba(46,163,212,0.45), transparent 70%),
      radial-gradient(ellipse 50% 25% at 70% 75%, rgba(46,163,212,0.35), transparent 70%),
      var(--cover-blue);
  }
  .back-cover__blurb {
    position: absolute;
    left: 74px;
    top: 90px;
    width: 393px;
    font-family: var(--text-font);
    font-weight: 700;
    font-size: 12.6px;
    line-height: 18.6px;
    letter-spacing: -0.1px;
    color: var(--paper);
    text-align: justify;
    hyphens: auto;
  }
  .back-cover__blurb p + p { margin-top: 18.6px; }

  .spine {
    position: relative;
    width: 66px;
    height: 100%;
    background: var(--ink);
  }
  .spine__line {
    position: absolute;
    left: 50%;
    writing-mode: vertical-rl;
    transform: translateX(-50%) rotate(180deg);
    white-space: nowrap;
  }
  .spine__subtitle {
    top: 28px;
    font-family: var(--text-font);
    font-size: 14px;
    color: var(--cover-blue);
  }
  .spine__title {
    top: 267px;
    font-family: var(--title-font);
    font-size: 34px;
    letter-spacing: 0.5px;
    color: var(--paper);
  }
  .spine__author {
    top: 573px;
    font-family: var(--text-font);
    font-size: 13px;
    color: var(--paper);
  }

  .front-cover__author {
    position: absolute;
    top: 36px;
    width: 100%;
    text-align: center;
    font-family: var(--text-font);
    font-weight: 700;
    font-size: 17px;
    color: var(--paper);
  }
  .front-cover__title {
    position: absolute;
    top: 80px;
    width: 100%;
    text-align: center;
    font-family: var(--title-font);
    font-weight: 400;
    font-size: 94px;
    line-height: 74px;
    color: var(--paper);
  }
  .front-cover__subtitle {
    position: absolute;
    top: 242px;
    width: 100%;
    text-align: center;
    font-family: var(--text-font);
    font-size: 17px;
    color: var(--ink);
  }
  .front-cover__art {
    position: absolute;
    left: 0;
    top: 0;
    width: 527px;
    height: 692px;
  }
</style>
</head>
<body>
  <main class="spread">
    <section class="back-cover">
      <div class="back-cover__blurb">
        <p>Lorem ipsum dolor sit amet, consectetur adipiscing elit. Proin lacinia tempus iaculis. Aenean facilisis tempus magna quis pharetra. Praesent dignissim ligula id tortor euismod, ut tempus risus pharetra. Phasellus imperdiet tristique nibh, a tempus metus lacinia non. In scelerisque, erat id sagittis egestas, magna nibh rhoncus justo, vitae commodo tortor risus sit amet ex. Donec id risus sodales, mattis nunc at, lobortis odio. Duis ut iaculis ligula. Aliquam sem dolor, hendrerit eu mauris sit amet, maximus suscipit urna. Duis ut libero risus.</p>
        <p>Integer diam velit, fermentum eget rhoncus molestie, vestibulum ut magna. Vivamus porta sollicitudin metus, non molestie orci blandit et. Sed eu viverra augue, a iaculis ipsum. Fusce malesuada molestie mauris vitae pellentesque. Nulla id lectus non libero volutpat placerat. Sed suscipit, orci eget efficitur aliquet, massa nibh faucibus enim, eget scelerisque elit justo a elit. Morbi eu blandit nunc. Quisque interdum orci ante, sed sagittis mi egestas vitae. Maecenas quis vulputate ex, at feugiat erat.</p>
      </div>
    </section>

    <section class="spine">
      <span class="spine__line spine__subtitle">and where your habits slip</span>
      <span class="spine__line spine__title">WAYS TO STAND OUT</span>
      <span class="spine__line spine__author">Tobar Kessly</span>
    </section>

    <section class="front-cover">
      <p class="front-cover__author">Tobar Kessly</p>
      <h1 class="front-cover__title">WAYS TO<br>STAND OUT</h1>
      <p class="front-cover__subtitle">and where your habits slip</p>
      <svg class="front-cover__art" viewBox="0 0 527 692">
        <defs>
          <linearGradient id="figure-tone" x1="0" y1="0" x2="0" y2="1">
            <stop offset="0" stop-color="#0c0e12"/>
            <stop offset="1" stop-color="#1a1d22"/>
          </linearGradient>
          <linearGradient id="reflection-tone" x1="0" y1="0" x2="1" y2="1">
            <stop offset="0" stop-color="#d9dadc"/>
            <stop offset="0.5" stop-color="#7d7f83"/>
            <stop offset="1" stop-color="#e6e7e8"/>
          </linearGradient>
        </defs>
        <polygon class="front-cover__door" points="269,352 446,286 446,692 269,692" fill="#0c0e12"/>
        <rect role="img" aria-label="Illustration: dark silhouetted figure looking toward the doorway" x="95" y="389" width="129" height="303" fill="url(#figure-tone)"/>
        <rect role="img" aria-label="Illustration: black and white spiral-striped reflection of the figure inside the doorway" x="292" y="389" width="137" height="303" fill="url(#reflection-tone)"/>
      </svg>
    </section>
  </main>
</body>
</html>
```